Minimalistic and chic product labels required for tea packaging

We need a Label Sticker Design for our tea company that is minimalistic, simple and chic.

We have 2 categories of tea: artisan tea (single flavoured tea e.g. green and black) and herbal teas (e.g. mixuture of herbs and flowers). We would like to have the designs to tell the difference of artisan tea and herbal tea, this can be done by having different colours to tell the difference or if there are other design features used.

We would also like to have colourful colours on our herbal tea range, preferably either a light and chic pastel colour palette or bright and chic colour palette.

The labels will be stuck onto a white pouch. The final design should also include the variety of colour palettes that can be used in AI format with the label. Preferred label measurements in 9cm width, and 11cm height. Our logo is attached.

Target Market(s)

Beauty and wellness

Industry/Entity Type

Health And Wellness

Requirements
Must have
• 2 x labels (front and back)
Front label must include logo, text to include tea type and weight
Back label must include text space to write description
Nice to have
• Simple and chic label design to stick onto a white pouch
Should not have
• Must not have too much graphic and pictures

```html
<!DOCTYPE html>
<html lang="en">
<head>
<meta charset="UTF-8">
<title>Leafhouse — Artisan Green Tea Label</title>
<link href="https://fonts.googleapis.com/css2?family=Allison&family=Jost:wght@300;400&display=swap" rel="stylesheet">
<style>
  :root {
    --page-bg: #f5f5f5;
    --label-top: #aed0cf;
    --label-mid: #98c3c6;
    --label-bottom: #86b8c2;
    --label-shade: #7e9fa2;
    --panel: #f4f4f4;
    --panel-edge: #e9e9e9;
    --script-teal: #8ecacb;
    --ink: #2e2e2e;
    --ink-soft: #4a4a4a;
  }
  * { margin: 0; padding: 0; box-sizing: border-box; }
  html, body {
    width: 900px;
    height: 1200px;
    overflow: hidden;
    background: var(--page-bg);
  }
  .canvas {
    position: relative;
    width: 900px;
    height: 1200px;
    background: var(--page-bg);
  }
  .label {
    position: absolute;
    left: 50px;
    top: 111px;
    width: 800px;
    height: 978px;
    overflow: hidden;
  }
  .label-art {
    position: absolute;
    inset: 0;
    width: 100%;
    height: 100%;
  }
  .brand-name {
    position: absolute;
    left: 0;
    width: 100%;
    top: 250px;
    text-align: center;
    font-family: 'Jost', sans-serif;
    font-weight: 300;
    font-size: 40px;
    letter-spacing: 2px;
    color: var(--ink);
  }
  .tea-type {
    position: absolute;
    left: 70px;
    top: 420px;
    font-family: 'Allison', cursive;
    font-size: 230px;
    line-height: 1;
    color: var(--script-teal);
  }
  .tea-variety {
    position: absolute;
    left: 408px;
    top: 602px;
    font-family: 'Jost', sans-serif;
    font-weight: 300;
    font-size: 27px;
    letter-spacing: 9px;
    color: var(--ink);
  }
  .weight-mark {
    position: absolute;
    left: 384px;
    top: 818px;
    width: 32px;
    height: 14px;
  }
  .net-weight {
    position: absolute;
    left: 0;
    width: 100%;
    top: 850px;
    text-align: center;
    font-family: 'Jost', sans-serif;
    font-weight: 300;
    font-size: 24px;
    color: var(--ink-soft);
  }
</style>
</head>
<body>
  <main class="canvas">
    <section class="label">
      <svg class="label-art" viewBox="0 0 800 978" xmlns="http://www.w3.org/2000/svg">
        <defs>
          <linearGradient id="label-fill" x1="0" y1="0" x2="0.35" y2="1">
            <stop offset="0" stop-color="var(--label-top)"/>
            <stop offset="0.55" stop-color="var(--label-mid)"/>
            <stop offset="1" stop-color="var(--label-bottom)"/>
          </linearGradient>
          <linearGradient id="label-shade" x1="0" y1="0" x2="1" y2="1">
            <stop offset="0.45" stop-color="var(--label-shade)" stop-opacity="0"/>
            <stop offset="1" stop-color="var(--label-shade)" stop-opacity="0.75"/>
          </linearGradient>
          <linearGradient id="panel-fill" x1="0" y1="0" x2="1" y2="1">
            <stop offset="0" stop-color="#f7f7f7"/>
            <stop offset="1" stop-color="var(--panel-edge)"/>
          </linearGradient>
        </defs>
        <rect class="label-ground" width="800" height="978" fill="url(#label-fill)" role="img" aria-label="Soft teal background with a faint repeating script pattern"/>
        <rect class="label-ground-shade" width="800" height="978" fill="url(#label-shade)"/>
        <polygon class="label-panel" points="401,41 766,169 766,812 401,936 33,812 33,169" fill="url(#panel-fill)"/>
      </svg>

      <div class="brand-name">Leafhouse</div>
      <div class="tea-type">Artisan</div>
      <div class="tea-variety">GREEN TEA</div>
      <svg class="weight-mark" viewBox="0 0 32 14" role="img" aria-label="Small leaf motif">
        <ellipse cx="18" cy="7" rx="12" ry="5" fill="none" stroke="var(--ink-soft)" stroke-width="1"/>
        <line x1="0" y1="7" x2="30" y2="7" stroke="var(--ink-soft)" stroke-width="1"/>
      </svg>
      <div class="net-weight">50g</div>
    </section>
  </main>
</body>
</html>
```